Mosquito and outdoor pest management

The uploaded logo must be integrated as the main theme of the card. I would like it to be modern and eye catching. Maybe some backround images or light silver metallic background.
Space enough at the base for contact info to be put in- phone numbers,emails,names,website.
Space on the back for short blog and lines for hand writing..calling card.
Commercial- golf courses, schools, outdoor function properties, pre event treatments.
Residential- retirement villages, townhome complexes and general houses
Management

```html
<!DOCTYPE html>
<html lang="en">
<head>
<meta charset="utf-8">
<title>Tallow Creek Mosquito – Business Card</title>
<link rel="stylesheet" href="https://fonts.googleapis.com/css2?family=Lato:wght@400;700;900&display=swap">
<style>
  :root {
    --page-bg: #2a2a2a;
    --card-light: #ffffff;
    --card-mid: #9a9a9a;
    --card-dark: #050505;
    --brand-red: #d0222b;
    --ink-dark: #2b2b2b;
    --ink-light: #f2f2f2;
    --ink-muted: #cfcfcf;
  }
  * { box-sizing: border-box; margin: 0; padding: 0; }
  html, body {
    width: 1200px;
    height: 997px;
    overflow: hidden;
    background: var(--page-bg);
    font-family: 'Lato', sans-serif;
  }
  .canvas {
    width: 1200px;
    height: 997px;
    display: flex;
    flex-direction: column;
    align-items: center;
    justify-content: center;
    gap: 60px;
  }
  .card {
    position: relative;
    width: 640px;
    height: 366px;
    border-radius: 4px;
    overflow: hidden;
    background: linear-gradient(180deg, var(--card-light) 0%, #e6e6e6 18%, var(--card-mid) 48%, #2a2a2a 72%, var(--card-dark) 100%);
    box-shadow: 0 14px 30px rgba(0, 0, 0, 0.55);
  }

  /* Brand name lockup */
  .brand {
    position: absolute;
    display: flex;
    align-items: center;
    gap: 10px;
    color: var(--ink-dark);
    font-weight: 700;
  }
  .brand-mark {
    width: 14px;
    height: 14px;
    background: var(--brand-red);
    flex: none;
  }
  .brand-name {
    font-size: 26px;
    line-height: 1;
    letter-spacing: 0.5px;
  }
  .brand-tagline {
    display: block;
    font-size: 10.5px;
    letter-spacing: 1px;
    text-transform: uppercase;
    margin-top: 5px;
  }

  /* Back side */
  .card--back .brand {
    left: 50%;
    top: 120px;
    transform: translateX(-50%);
  }

  /* Front side */
  .card--front .brand {
    right: 34px;
    top: 46px;
  }
  .person {
    position: absolute;
    right: 34px;
    top: 172px;
    text-align: right;
  }
  .person-name {
    color: var(--brand-red);
    font-weight: 900;
    font-size: 19px;
    letter-spacing: 1px;
    text-transform: uppercase;
  }
  .person-role {
    color: var(--ink-light);
    font-weight: 700;
    font-size: 13px;
    letter-spacing: 1px;
    text-transform: uppercase;
    margin-top: 3px;
  }
  .contact-tab {
    position: absolute;
    left: 0;
    top: 236px;
    width: 42px;
    height: 118px;
    background: var(--brand-red);
    border-radius: 0 12px 12px 0;
    display: flex;
    flex-direction: column;
    align-items: center;
    justify-content: space-around;
    padding: 10px 0;
  }
  .contact-tab svg {
    width: 15px;
    height: 15px;
    fill: none;
    stroke: var(--ink-light);
    stroke-width: 1.8;
    stroke-linecap: round;
    stroke-linejoin: round;
  }
  .contact-list {
    position: absolute;
    left: 74px;
    top: 222px;
    list-style: none;
    color: var(--ink-light);
    font-weight: 700;
    font-size: 14px;
    line-height: 1.2;
  }
  .contact-list li { margin-bottom: 11px; }
  .contact-list li:last-child { margin-bottom: 0; }
</style>
</head>
<body>
<main class="canvas">

  <section class="card card--back" aria-label="Business card, back">
    <div class="brand">
      <span class="brand-mark"></span>
      <div>
        <span class="brand-name">Tallow Creek Mosquito</span>
        <span class="brand-tagline">and Outdoor Pest Management</span>
      </div>
    </div>
  </section>

  <section class="card card--front" aria-label="Business card, front">
    <div class="brand">
      <span class="brand-mark"></span>
      <div>
        <span class="brand-name">Tallow Creek Mosquito</span>
        <span class="brand-tagline">and Outdoor Pest Management</span>
      </div>
    </div>

    <div class="person">
      <p class="person-name">Lena Marsh</p>
      <p class="person-role">Director</p>
    </div>

    <div class="contact-tab" aria-hidden="true">
      <svg viewBox="0 0 16 16"><path d="M2 6c0-2 2.5-3 6-3s6 1 6 3l-2 1-1-2H5L4 7 2 6z"/><path d="M4 8h8l1 5H3z"/><circle cx="8" cy="10.5" r="1.2"/></svg>
      <svg viewBox="0 0 16 16"><path d="M2 6c0-2 2.5-3 6-3s6 1 6 3l-2 1-1-2H5L4 7 2 6z"/><path d="M4 8h8l1 5H3z"/><circle cx="8" cy="10.5" r="1.2"/></svg>
      <svg viewBox="0 0 16 16"><rect x="2" y="4" width="12" height="9" rx="1"/><path d="M2 4l6 5 6-5"/></svg>
      <svg viewBox="0 0 16 16"><path d="M7 9.5a3 3 0 0 0 4 0l2.5-2.5a3 3 0 0 0-4-4L8.5 4"/><path d="M9 6.5a3 3 0 0 0-4 0L2.5 9a3 3 0 0 0 4 4l1-1"/></svg>
    </div>

    <ul class="contact-list">
      <li>305.555.0142</li>
      <li>954.555.0187</li>
      <li>lena@tallowcreek.com</li>
      <li>4810 Harbor Ave. Miami,<br>FL 33150</li>
    </ul>
  </section>

</main>
</body>
</html>
```